Shipping and Logistics, Project

Project description : Company Profile

A total logistics company covering domestic / international freight forwarding, warehouse management services, haulage, supply chain management, transport management & distribution, procurement & assembly services, shipping, chartering & bunker services, project logistics & tax exemption consultancy, oil & gas logistics, halal logistics services & integrated logistics management. We’re a well-established and experienced freight forwarder in Kuala Lumpur, Malaysia. We specialize in customized value-added solution that optimizes your supply chain by trimming inventory, reducing logistics cost and enhancing your customer service levels.

As a member of the Worldwide Carrier and Haulage Alliance which comprise of 170 global freight agents in 80 countries that promotes great handling in cross-trade logistics and freighting. You could rely on our efficiency in handlings of export cargo (FCL, LCL, Bulk and Conventional) between our global network offices worldwide with a total scale of 10,000 groomed specialists in various logistics division working together to ensure delivery task meets with your expectation. With our dedicated qualified and experienced professionals, we are fully committed to serving our clients.

Our generic services are listed below for your reference:

• Air Freight
• Ocean Freight FCL & LCL
• Container Haulage
• Warehousing
• Transportation and Distribution within Malaysia and Thailand
• Cross-Border Road Line-hauls between Thailand, Malaysia, Singapore and Laos
• Customs Brokerage and Forwarding
• Project Cargo Freight Forwarding for setting up of new plants / factories and ad hoc heavy-lift
• Air-Sea-Road-Rail multi-modal options
• Import / Export / Storage / Documentation / Handling of DG / Hazmat
• Vessel and Aircraft Charters

Our Mission
Based on the motto “Quick, Reliable and Polite”, we are dedicated to upholding the following three points corporate philosophy:
1. Adhering to the principle that “the customer always comes first”.
2. Contributing to the development of the local community.
3. Making it our duty to be responsible and sincere.

Our Edge
• One-Stop Logistics Solutions
• Extensive Network Throughout Malaysia
• Highly Qualified and Experienced Pool of Professionals
• Comprehensive IT Solutions
• Innovative and Customer-focused Solutions
• Flexible and Consistent in Managing Exceptions
• Total Supply Chain Visibility

Target Market
1. We sell the logistics services to all the industry in Malaysia and Worldwide. (ONE Stop Logistics Solutions)

Competitor
1. RT Volmaren
2. Corvella Transport
3. Brandt + Osswig
4. VELIRO
5. TZQ
6. Farrowline
7. Ruma Logistics

Rules for Picking a Company Name
1. Unique and unforgettable
2. Avoid unusual spellings
3. Easy to pronounce and remember
4. Keep it simple
5. Make some sense
6. Give a clue

Rules for Picking a Company Logo
4. Keep it simple
5. Make some sense
6. Give a clue

1. Simplicity
2. Memorability
3. Originality
4. Modern Yet Timeless
5. Balance
6. Complementary
7. Versatility

Stationery Information
1. Company Name : Tepiandek Solutions Sdn Bhd
2. Company Registration : 2730518-W
3. Address : 14-07, Jalan Seroja Indah 5, Taman Bukit Seroja, 81300 Johor Bahru, Johor, Malaysia.
4. Name : Derek Tan
5. Position : Manager
6. Mobile No : (+6019) 4308127
7. Office No : (+607) 5129870
8. Fax No : Not Available
9. Email Address : derek.tan@tepiandek-freight.example
10. Web Domain : www.tepiandek-freight.example
11. Company Slogan : Be Globally Connected

Target Market(s)

Corporate Company

Industry/Entity Type

Shipping and Logistics Industry

Requirements
Must have
• Company Full Name : TEPIANDEK SOLUTIONS SDN. BHD.
Nice to have
• Keep it simple and unforgettable ...

```html
<!DOCTYPE html>
<html lang="en">
<head>
<meta charset="UTF-8">
<title>Tepiandek Solutions – Business Card</title>
<link rel="stylesheet" href="https://fonts.googleapis.com/css2?family=Poppins:wght@500;600&family=Source+Sans+3:wght@400&display=swap">
<style>
  :root {
    --backdrop: #8a8a8a;
    --card-light: #ffffff;
    --card-dark: #262626;
    --brand-blue: #2f86d8;
    --ink: #222222;
    --ink-light: #ffffff;
  }
  * { margin: 0; padding: 0; box-sizing: border-box; }
  html, body {
    width: 1093px;
    height: 1200px;
    overflow: hidden;
    background: var(--backdrop);
  }
  .canvas { position: relative; width: 1093px; height: 1200px; }

  .card {
    position: absolute;
    left: 265px;
    width: 578px;
    height: 356px;
    border-radius: 24px;
    overflow: hidden;
  }
  .card--front { top: 226px; background: var(--card-light); }
  .card--back  { top: 621px; background: var(--card-dark); }

  /* Person */
  .person { position: absolute; left: 31px; top: 48px; }
  .person__name {
    font-family: "Poppins", sans-serif;
    font-weight: 600;
    font-size: 24px;
    line-height: 1.1;
    color: var(--brand-blue);
    letter-spacing: 0.2px;
  }
  .person__role {
    font-family: "Source Sans 3", sans-serif;
    font-size: 16px;
    color: var(--ink);
    margin-top: 1px;
  }

  /* Wordmark */
  .wordmark {
    display: flex;
    align-items: center;
    gap: 12px;
    font-family: "Poppins", sans-serif;
    font-weight: 500;
  }
  .wordmark__mark {
    width: 40px;
    height: 40px;
    background: var(--brand-blue);
    flex: none;
  }
  .wordmark__text { display: flex; flex-direction: column; line-height: 1; }
  .wordmark__name { letter-spacing: 0.5px; }
  .wordmark__sub { letter-spacing: 0.62em; margin-top: 4px; }

  .card--front .wordmark {
    position: absolute;
    right: 31px;
    top: 40px;
    color: var(--ink);
  }
  .card--front .wordmark__name { font-size: 29px; }
  .card--front .wordmark__sub { font-size: 14px; margin-right: -0.62em; }

  .registration {
    position: absolute;
    right: 31px;
    top: 126px;
    font-family: "Source Sans 3", sans-serif;
    font-size: 16px;
    color: var(--ink);
  }
  .registration__label { color: var(--brand-blue); }

  /* Contacts */
  .contacts {
    position: absolute;
    left: 31px;
    top: 248px;
    list-style: none;
    font-family: "Source Sans 3", sans-serif;
    font-size: 16.5px;
    color: var(--ink);
  }
  .contacts__item {
    display: flex;
    align-items: center;
    gap: 6px;
    height: 21px;
  }
  .contacts__icon { width: 15px; height: 15px; flex: none; }

  .address {
    position: absolute;
    right: 31px;
    top: 247px;
    font-family: "Source Sans 3", sans-serif;
    font-size: 16.5px;
    line-height: 21px;
    color: var(--ink);
    text-align: right;
    font-style: normal;
  }

  /* Back */
  .card--back .wordmark {
    position: absolute;
    left: 50%;
    top: 142px;
    transform: translateX(-50%);
    color: var(--ink-light);
    gap: 16px;
  }
  .card--back .wordmark__mark { width: 54px; height: 54px; }
  .card--back .wordmark__name { font-size: 37px; }
  .card--back .wordmark__sub { font-size: 18px; margin-right: -0.62em; }

  .slogan {
    position: absolute;
    left: 0;
    right: 0;
    top: 287px;
    text-align: center;
    font-family: "Poppins", sans-serif;
    font-weight: 500;
    font-size: 20px;
    color: var(--brand-blue);
    letter-spacing: 0.3px;
  }
</style>
</head>
<body>
<main class="canvas">

  <section class="card card--front" aria-label="Business card front">
    <div class="person">
      <h1 class="person__name">DEREK TAN</h1>
      <p class="person__role">Manager</p>
    </div>

    <div class="wordmark">
      <span class="wordmark__mark" aria-hidden="true"></span>
      <span class="wordmark__text">
        <span class="wordmark__name">TEPIANDEK</span>
        <span class="wordmark__sub">SOLUTIONS</span>
      </span>
    </div>

    <p class="registration"><span class="registration__label">Registration :</span> 2730518-W</p>

    <ul class="contacts">
      <li class="contacts__item">
        <svg class="contacts__icon" viewBox="0 0 16 16" aria-hidden="true">
          <rect x="3.5" y="1" width="9" height="14" rx="1.5" fill="none" stroke="#2f86d8" stroke-width="1.5"/>
          <circle cx="8" cy="12.5" r="0.9" fill="#2f86d8"/>
        </svg>
        (+6019) 4308127
      </li>
      <li class="contacts__item">
        <svg class="contacts__icon" viewBox="0 0 16 16" aria-hidden="true">
          <path d="M4 1.5 L6.5 4.5 L5 6.5 Q6.5 9.5 9.5 11 L11.5 9.5 L14.5 12 L12.5 14.5 Q6 14 1.5 3.5 Z" fill="none" stroke="#2f86d8" stroke-width="1.4" stroke-linejoin="round"/>
          <path d="M9.5 3 A4 4 0 0 1 13 6.5 M9.5 0.8 A6 6 0 0 1 15.2 6.5" fill="none" stroke="#2f86d8" stroke-width="1.2"/>
        </svg>
        (+607) 5129870
      </li>
      <li class="contacts__item">
        <svg class="contacts__icon" viewBox="0 0 16 16" aria-hidden="true">
          <rect x="0.5" y="3" width="15" height="10" fill="#2f86d8"/>
          <path d="M0.5 3 L8 9 L15.5 3" fill="none" stroke="#fff" stroke-width="1.2"/>
        </svg>
        derek.tan@tepiandek-freight.example
      </li>
      <li class="contacts__item">
        <svg class="contacts__icon" viewBox="0 0 16 16" aria-hidden="true">
          <g fill="none" stroke="#2f86d8" stroke-width="1.2">
            <circle cx="8" cy="8" r="7"/>
            <ellipse cx="8" cy="8" rx="3" ry="7"/>
            <path d="M1 8 H15 M2 4.5 H14 M2 11.5 H14"/>
          </g>
        </svg>
        www.tepiandek-freight.example
      </li>
    </ul>

    <address class="address">
      14-07, Jalan Seroja Indah 5<br>
      Taman Bukit Seroja<br>
      81300 Johor Bahru<br>
      Johor, Malaysia
    </address>
  </section>

  <section class="card card--back" aria-label="Business card back">
    <div class="wordmark">
      <span class="wordmark__mark" aria-hidden="true"></span>
      <span class="wordmark__text">
        <span class="wordmark__name">TEPIANDEK</span>
        <span class="wordmark__sub">SOLUTIONS</span>
      </span>
    </div>
    <p class="slogan">BE GLOBALLY CONNECTED</p>
  </section>

</main>
</body>
</html>
```